Trade Alert Service needs Vistrel thumbnail / channel design

I'm about to set up a Vistrel channel which gives real-time trade alerts to earn passive income. I'm looking for a Vistrel channel design to include thumbnail and other associated visuals for the channel.
The trade alerts will be focused around selling cash-secured put options on US equities, and directed at people who want investing advice / tips for getting out of the rat race. I'd like the theme to be somewhat serious / credible, without too many eye-popping neon colours like all the other cheap trade alert videos / day trading videos on Vistrel. Happy for you to use your experience if you think otherwise though, as you're the designer, not me!

Target Market(s)

Option Traders, Value Investors, People who want passive income

Industry/Entity Type

Finance

Logo Text

Calm Meadow Wealth Notes

Requirements
Must have
• All relevant Vistrel visuals so that I can upload them to the Vistrel channel - all visuals required by Vistrel Studio upload within the channel creation page.
A logo so that I can append it to Powerpoint presentations
Nice to have
• A blank Powerpoint slide template showing the logo would be great in chosen colour scheme

```html
<!DOCTYPE html>
<html lang="en">
<head>
<meta charset="utf-8">
<title>Calm Meadow Wealth Notes – Vistrel Thumbnails</title>
<link href="https://fonts.googleapis.com/css2?family=Anton&family=Archivo+Black&family=Baloo+2:wght@800&display=swap" rel="stylesheet">
<style>
  :root {
    --stage: #2a2c30;
    --pink: #c85a9e;
    --pink-light: #d77bb3;
    --pink-dark: #a8457f;
    --blue: #4a72dc;
    --blue-light: #6a8ee6;
    --blue-dark: #3a5cc4;
    --white: #ffffff;
  }
  * { box-sizing: border-box; margin: 0; padding: 0; }
  html, body { width: 1200px; height: 675px; overflow: hidden; }
  body {
    background: var(--stage);
    display: flex;
    align-items: center;
    justify-content: center;
    gap: 30px;
  }
  .thumbnail {
    position: relative;
    width: 555px;
    height: 312px;
    overflow: hidden;
    color: var(--white);
  }
  .thumbnail__photo {
    position: absolute;
    inset: 0;
  }
  .thumbnail--pink .thumbnail__photo {
    background: linear-gradient(110deg, var(--pink) 0%, var(--pink-light) 45%, var(--pink-dark) 100%);
  }
  .thumbnail--blue .thumbnail__photo {
    background: linear-gradient(110deg, var(--blue) 0%, var(--blue-light) 60%, var(--blue-dark) 100%);
  }
  .headline { position: absolute; left: 22px; top: 26px; }
  .headline--condensed {
    font-family: "Anton", sans-serif;
    text-transform: uppercase;
    line-height: 0.95;
  }
  .headline__kicker { font-size: 34px; display: block; }
  .headline__main { font-size: 96px; display: block; }
  .headline--rounded .headline__lead {
    font-family: "Baloo 2", sans-serif;
    font-weight: 800;
    font-size: 46px;
    line-height: 0.95;
    display: block;
    letter-spacing: -0.5px;
  }
  .headline--rounded .headline__main {
    font-family: "Archivo Black", sans-serif;
    font-size: 66px;
    line-height: 1.05;
    letter-spacing: -1.5px;
  }
  .brand {
    position: absolute;
    right: 18px;
    bottom: 16px;
    display: flex;
    align-items: flex-end;
    gap: 8px;
    font-family: "Anton", sans-serif;
    text-transform: uppercase;
    font-size: 30px;
    line-height: 0.95;
    text-align: right;
    color: var(--white);
  }
  .brand__mark {
    width: 14px;
    height: 14px;
    background: var(--white);
    margin-bottom: 6px;
  }
</style>
</head>
<body>
  <section class="thumbnail thumbnail--pink">
    <div class="thumbnail__photo" role="img" aria-label="Pink-tinted photo of a woman working at a desk in a bright home office"></div>
    <h2 class="headline headline--condensed">
      <span class="headline__kicker">Best Investing</span>
      <span class="headline__main">Advice</span>
    </h2>
    <div class="brand">
      <span class="brand__mark"></span>
      <span class="brand__name">Calm Meadow<br>Wealth Notes</span>
    </div>
  </section>

  <section class="thumbnail thumbnail--blue">
    <div class="thumbnail__photo" role="img" aria-label="Blue-tinted photo of a bearded man reading at a desk with a lamp"></div>
    <h2 class="headline headline--rounded">
      <span class="headline__lead">Tips for getting<br>out of the</span>
      <span class="headline__main">RAT RACE</span>
    </h2>
    <div class="brand">
      <span class="brand__mark"></span>
      <span class="brand__name">Calm Meadow<br>Wealth Notes</span>
    </div>
  </section>
</body>
</html>
```